Graphic to show easy steps to find financial clarity

Howdy-I need a graphic that describe my Coin Compass Method.The attached is a concept, but please use your own creativity to show how you would display this:- There are 5 steps the process (and then we repeat/recalculate)- And three bullets that drive home the results of the processI've also attached my logo. Please use the colors in my logo and maybe add a soft green as needed.The reader should be able to briefly scan this document and understand that this is an easy/simple process that tells them how to manage their cash.Thanks!-Ned

Target Market(s)

wealthy women, whether single or married

Requirements
Must have
• Please use the colors in my logo and a soft green if needed
Should not have
• This should be a very easy to read graphic that communicates how simple/easy this is to do.

```html
<!DOCTYPE html>
<html lang="en">
<head>
<meta charset="utf-8">
<title>Coin Compass Method</title>
<link href="https://fonts.googleapis.com/css2?family=Montserrat:wght@600&family=Lato:wght@400&display=swap" rel="stylesheet">
<style>
  :root {
    --navy: #0a3a7c;
    --green: #7dbf7f;
    --green-soft: #96d698;
    --slate: #666666;
    --paper: #ffffff;
    --bg-edge: #e4e4e4;
  }
  html, body { margin: 0; padding: 0; overflow: hidden; }
  body { width: 1200px; height: 889px; }
  .canvas {
    position: relative;
    width: 1200px;
    height: 889px;
    overflow: hidden;
    background: radial-gradient(ellipse at 50% 50%, #fafafa 0%, #f2f2f2 45%, var(--bg-edge) 100%);
    font-family: "Lato", sans-serif;
  }
  .title {
    position: absolute;
    top: 36px; left: 0; width: 100%;
    margin: 0;
    text-align: center;
    font-family: "Montserrat", sans-serif;
    font-weight: 600;
    font-size: 39px;
    letter-spacing: 7px;
    color: var(--navy);
    text-transform: uppercase;
  }
  .flow { position: absolute; inset: 0; }
  .step-label {
    position: absolute;
    display: flex; align-items: center; justify-content: center;
    height: 61px;
    border-radius: 31px;
    background: var(--navy);
    color: var(--paper);
    font-size: 19px;
    line-height: 23px;
    text-align: center;
    text-transform: uppercase;
  }
  .result {
    position: absolute;
    display: flex; align-items: center; justify-content: center;
    height: 38px;
    border-radius: 19px;
    background: var(--slate);
    color: var(--paper);
    font-size: 21px;
    text-transform: uppercase;
    white-space: nowrap;
  }
</style>
</head>
<body>
<div class="canvas">
  <h1 class="title">Coin Compass Method</h1>

  <svg class="flow" width="1200" height="889" viewBox="0 0 1200 889">
    <defs>
      <linearGradient id="hexRim" gradientUnits="userSpaceOnUse" x1="0" y1="366" x2="0" y2="510">
        <stop offset="0.25" stop-color="#96d698"/>
        <stop offset="0.8" stop-color="#666666"/>
      </linearGradient>
      <marker id="tipGreen" viewBox="0 0 10 10" refX="5" refY="9" markerWidth="8" markerHeight="8" orient="auto-start-reverse">
        <path d="M0,0 L5,10 L10,0 L5,4 Z" fill="#96d698"/>
      </marker>
    </defs>

    <!-- connectors from labels -->
    <g class="connectors" stroke="#4a6a8a" stroke-width="1.5">
      <line x1="170" y1="297" x2="170" y2="357" marker-end="url(#tipGreen)"/>
      <line x1="335" y1="208" x2="335" y2="357" marker-end="url(#tipGreen)"/>
      <line x1="497" y1="297" x2="497" y2="357" marker-end="url(#tipGreen)"/>
      <line x1="665" y1="208" x2="665" y2="357" marker-end="url(#tipGreen)"/>
      <line x1="827" y1="297" x2="827" y2="357" marker-end="url(#tipGreen)"/>
      <line x1="994" y1="208" x2="994" y2="357" marker-end="url(#tipGreen)"/>
    </g>

    <!-- hexagon chain -->
    <g class="hex-chain" fill="#ffffff" stroke="url(#hexRim)" stroke-width="18" stroke-linejoin="round">
      <path d="M86,438 L122,373 L218,373 L254,438 L218,503 L122,503 Z"/>
      <path d="M251,438 L287,373 L383,373 L419,438 L383,503 L287,503 Z"/>
      <path d="M413,438 L449,373 L545,373 L581,438 L545,503 L449,503 Z"/>
      <path d="M581,438 L617,373 L713,373 L749,438 L713,503 L617,503 Z"/>
      <path d="M743,438 L779,373 L875,373 L911,438 L875,503 L779,503 Z"/>
      <path d="M910,438 L946,373 L1042,373 L1078,438 L1042,503 L946,503 Z"/>
    </g>

    <!-- step icons -->
    <g class="icons" fill="#7dbf7f" stroke="none">
      <!-- money with up/down arrows -->
      <g transform="translate(170,438)">
        <rect x="-26" y="-18" width="50" height="30" rx="3" transform="rotate(8)"/>
        <circle cx="-1" cy="-2" r="9" fill="#fff"/>
        <text x="-1" y="3" font-size="13" font-family="Lato, sans-serif" text-anchor="middle" fill="#7dbf7f">$</text>
        <path d="M-27,-40 L-18,-30 L-23,-30 L-23,-22 L-31,-22 L-31,-30 L-36,-30 Z"/>
        <path d="M18,36 L9,26 L14,26 L14,18 L22,18 L22,26 L27,26 Z"/>
      </g>
      <!-- wallet -->
      <g transform="translate(335,438)">
        <rect x="-14" y="-36" width="26" height="18" rx="2" transform="rotate(-30)"/>
        <path d="M-35,-8 L22,-20 L22,12 L-35,26 Z"/>
        <path d="M-30,-3 L16,-13 L16,6 L-30,19 Z" fill="#fff"/>
        <path d="M-26,2 L12,-7 L12,-4 L-26,5 Z"/>
      </g>
      <!-- calendar with bills -->
      <g transform="translate(497,438)">
        <rect x="-33" y="-30" width="66" height="62" rx="5"/>
        <rect x="-27" y="-16" width="54" height="42" rx="2" fill="#fff"/>
        <rect x="-19" y="-38" width="6" height="14" rx="3"/>
        <rect x="13" y="-38" width="6" height="14" rx="3"/>
        <rect x="-20" y="-6" width="38" height="22" rx="2" transform="rotate(12)"/>
        <circle cx="0" cy="6" r="6" fill="#fff"/>
      </g>
      <!-- hand with coin -->
      <g transform="translate(665,438)">
        <circle cx="0" cy="-21" r="17"/>
        <text x="0" y="-14" font-size="21" font-family="Lato, sans-serif" text-anchor="middle" fill="#fff">$</text>
        <rect x="-44" y="10" width="7" height="22"/>
        <path d="M-35,12 C-20,6 -8,8 4,14 L18,14 C22,14 22,20 18,20 L2,20 L2,22 L20,22 L38,12 C42,10 45,14 42,16 L22,30 L-35,30 Z"/>
      </g>
      <!-- plant with coin -->
      <g transform="translate(827,438)">
        <circle cx="3" cy="-29" r="13"/>
        <text x="3" y="-23" font-size="16" font-family="Lato, sans-serif" text-anchor="middle" fill="#fff">$</text>
        <rect x="1" y="-16" width="3" height="28"/>
        <path d="M1,0 C-8,-12 -22,-12 -27,-10 C-22,2 -8,4 1,0 Z"/>
        <path d="M4,-4 C12,-14 26,-14 30,-12 C24,-2 12,0 4,-4 Z"/>
        <rect x="-20" y="10" width="44" height="9" rx="2"/>
        <path d="M-15,19 L19,19 L15,44 L-11,44 Z"/>
      </g>
      <!-- document with pencil -->
      <g transform="translate(994,438)">
        <path d="M-24,-34 L18,-34 L18,-10 L10,2 L10,-26 L-14,-26 L-24,-16 Z"/>
        <path d="M-26,-18 L-14,-30 L-14,30 L6,30 L2,36 L-26,36 Z"/>
        <rect x="-8" y="-18" width="20" height="3"/>
        <rect x="-8" y="-10" width="20" height="3"/>
        <rect x="-20" y="-2" width="24" height="3"/>
        <rect x="-20" y="6" width="18" height="3"/>
        <rect x="-20" y="14" width="14" height="3"/>
        <path d="M24,-4 L31,3 L8,28 L0,31 L2,22 Z"/>
      </g>
    </g>

    <!-- results connector -->
    <g class="results-connector" stroke="#666666" stroke-width="1.5" fill="none">
      <path d="M1087,438 L1129,438 L1129,780 L1037,780"/>
      <line x1="1129" y1="651" x2="805" y2="651"/>
      <line x1="1129" y1="716" x2="920" y2="716"/>
    </g>
    <g class="arrow-tips" fill="#666666">
      <path d="M1129,572 L1123,556 L1129,561 L1135,556 Z"/>
      <path d="M962,651 L978,645 L973,651 L978,657 Z"/>
      <path d="M1025,716 L1041,710 L1036,716 L1041,722 Z"/>
      <path d="M1059,780 L1075,774 L1070,780 L1075,786 Z"/>
    </g>
  </svg>

  <div class="step-label" style="left:57px; top:236px; width:224px;">Know your<br>annual spending</div>
  <div class="step-label" style="left:230px; top:148px; width:194px;">Project simple<br>expenses</div>
  <div class="step-label" style="left:390px; top:236px; width:215px;">Add up your 5<br>year cash needs</div>
  <div class="step-label" style="left:567px; top:148px; width:192px;">Set them aside<br>in savings</div>
  <div class="step-label" style="left:767px; top:236px; width:133px;">Invest<br>the rest</div>
  <div class="step-label" style="left:907px; top:148px; width:168px;">Recalculate<br>monthly</div>

  <div class="result" style="left:361px; top:632px; width:444px;">Spend intentionally and with joy</div>
  <div class="result" style="left:245px; top:697px; width:675px;">Create a sold base for lifetime cash flow projections</div>
  <div class="result" style="left:128px; top:762px; width:909px;">Know your lifestyle will be unaffected by the markets for atleast 5 years</div>
</div>
</body>
</html>
```